business stationery for email layout
startup company
Simple
RT
Via G. Morelli, 17
26813 Borgoriva PV
Italy
Info@Tallimora.com
www.tallimora.com
minimalist, retail, fashion, technology, internet, innovative,one-step ahead, easy, intuitive, immediate, serious,credible
logo blue version
logo grey version
symbol blue version
symbol grey version

```html
<!DOCTYPE html>
<html lang="en">
<head>
<meta charset="utf-8">
<title>Tallimora – Business Card</title>
<link rel="stylesheet" href="https://fonts.googleapis.com/css2?family=Open+Sans:wght@400;700&display=swap">
<style>
  :root {
    --backdrop: #363636;
    --card: #ffffff;
    --brand-blue: #2b7fc1;
    --label-blue: #1f5f9e;
    --ink: #222222;
  }
  * { margin: 0; padding: 0; box-sizing: border-box; }
  html, body {
    width: 1200px;
    height: 814px;
    overflow: hidden;
    background: var(--backdrop);
    font-family: "Open Sans", Arial, sans-serif;
  }
  .canvas {
    position: relative;
    width: 1200px;
    height: 814px;
  }
  .business-card {
    position: absolute;
    left: 190px;
    top: 173px;
    width: 820px;
    height: 468px;
    background: var(--card);
  }
  .brand-mark {
    position: absolute;
    left: 42px;
    top: 410px;
    transform: rotate(-90deg);
    transform-origin: left top;
    display: flex;
    align-items: center;
    gap: 12px;
    white-space: nowrap;
    height: 50px;
  }
  .brand-dot {
    width: 26px;
    height: 26px;
    border-radius: 50%;
    background: var(--brand-blue);
  }
  .brand-name {
    font-size: 46px;
    font-weight: 400;
    color: var(--brand-blue);
    letter-spacing: 3px;
    line-height: 1;
    text-transform: uppercase;
  }
  .contact-block {
    position: absolute;
    left: 484px;
    top: 280px;
    color: var(--ink);
  }
  .contact-initials {
    font-size: 28px;
    font-weight: 700;
    color: var(--label-blue);
    line-height: 1.2;
    margin-bottom: 2px;
  }
  .contact-row {
    display: flex;
    font-size: 16px;
    line-height: 24.5px;
  }
  .contact-label {
    width: 70px;
    font-weight: 700;
    color: var(--label-blue);
  }
  .contact-address {
    font-size: 16px;
    line-height: 26px;
  }
</style>
</head>
<body>
<main class="canvas">
  <section class="business-card">
    <div class="brand-mark">
      <span class="brand-dot"></span>
      <span class="brand-name">Tallimora</span>
    </div>
    <div class="contact-block">
      <p class="contact-initials">RT</p>
      <p class="contact-row"><span class="contact-label">Phone:</span><span>+390298316402</span></p>
      <p class="contact-row"><span class="contact-label">Fax:</span><span>+390298316459</span></p>
      <p class="contact-row"><span class="contact-label">Email:</span><span>Info@Tallimora.com</span></p>
      <p class="contact-row"><span class="contact-label">Web:</span><span>www.tallimora.com</span></p>
      <p class="contact-address">Via G. Morelli, 17 26813 Borgoriva PV Italy</p>
    </div>
  </section>
</main>
</body>
</html>
```